Mexican Crafts and Fashion Ecommerce store

We need the design of a store where we can post our inventory products through a store with diferent categories MEN,Women, Jewelery, Religion, Crafts Home DEcorations, Snapbacks Hats. And a space to dedicate to all of our Mexican Hand Crafters that spend days decorating unique designs.
We have 3 locations open now so we need to manage inventory in those diferent locations, and we have different workers that work throught comission so its important to know who sold it and been able to manage their weekly sales. that they can upload pictures of new products with the prices with their phone or tabro.
We want something luxury but clean not loosing the cultural design we already have a logo and would need to transfer the domain from plinko to vendora, we want to be able to sell in Chatterly and as many places as we can and if we open a new location being able to include the inventory or transfer from store to store that the client can buy and see the shipping cost online we normally use nqrs or frx.
I will atach picture of our logo and the picture of some stuff that we already have in stock, Please put an option to sell internationally.
We will also require to work in android and Zelvo
We want vendora since it has really good reviews but want something easy for anyone without experience to use.

Target Market(s)

sell as much as possible andbe able to have online inventory

Industry/Entity Type

Fashion

Font styles to use
Serif
Sans Serif
Script

Colors

Designer to choose colors to be used in the design.

Requirements
Must have
• Online store, 3 locations inventory, luxury look but keep the cultural style not in the sobrero and boots style the cultural style that represents aztecs, painters, and more in the urban style.
Nice to have
• we will like to see our culture represented and an easy way to sell internationally in an easy manner.
• Customer tracking

```html
<!DOCTYPE html>
<html lang="en">
<head>
<meta charset="utf-8">
<title>Casa Lumbre — Mexican Crafts &amp; Fashion</title>
<link rel="stylesheet" href="https://fonts.googleapis.com/css2?family=Yellowtail&family=PT+Serif:wght@400;700&family=Source+Sans+3:wght@300;400;600;700&display=block">
<style>
  :root{
    --ink:#0e0e0e;
    --header:#151515;
    --footer:#1a1a1a;
    --white:#ffffff;
    --muted:#9a9a9a;
    --text:#555555;
    --title:#5a5a5a;
    --cyan:#1cc3ee;
    --yellow:#f6b820;
    --green:#8cc63e;
    --red:#d0232a;
    --card:#efefef;
    --line:#3a3a3a;
  }
  *{box-sizing:border-box;margin:0;padding:0}
  html,body{width:1200px;height:3030px;overflow:hidden}
  body{position:relative;background:var(--white);font-family:"Source Sans 3",Arial,sans-serif;color:var(--text)}
  .photo{position:absolute;display:block}

  /* header */
  .site-header{position:absolute;left:0;top:0;width:1200px;height:150px;background:radial-gradient(ellipse at 50% 40%,#2a2a2a 0%,var(--header) 60%,#0b0b0b 100%)}
  .nav{position:absolute;top:66px;display:flex;align-items:center;gap:7px;color:var(--white);font-size:11px;white-space:nowrap}
  .nav svg{display:block}
  .brand{position:absolute;left:440px;top:52px;width:320px;text-align:center;display:flex;align-items:center;justify-content:center;gap:10px;color:var(--yellow);font-family:"PT Serif",Georgia,serif;font-weight:700;font-size:30px;letter-spacing:1px;white-space:nowrap}
  .brand-dot{width:14px;height:14px;border-radius:50%;background:var(--yellow);flex:none}

  /* hero */
  .hero{position:absolute;left:0;top:150px;width:1200px;height:520px;background:linear-gradient(90deg,#3b3532 0%,#d9d2cc 22%,#efeae4 40%,#e8e1d8 60%,#c6413c 80%,#3a2c2a 100%)}
  .hero-title{position:absolute;left:0;top:196px;width:1200px;height:160px;text-align:center}
  .hero-script{font-family:"Yellowtail","Kaushan Script",cursive;color:var(--yellow);font-size:140px;line-height:1;display:block;margin-left:-10px;font-weight:400}
  .hero-sub{position:absolute;left:548px;top:120px;font-family:"Source Sans 3",sans-serif;font-weight:300;color:var(--white);font-size:38px;white-space:nowrap}

  /* stores */
  .stores{position:absolute;left:0;top:670px;width:1200px;height:158px;background:var(--ink)}
  .store{position:absolute;top:36px;width:250px;text-align:center;color:var(--white)}
  .store svg{display:block;margin:0 auto 8px}
  .store-name{font-size:12px;font-weight:600}
  .store-addr{font-size:10px;color:#cfcfcf;line-height:16px;margin-top:4px}
  .store-sep{position:absolute;top:30px;width:1px;height:96px;background:var(--line)}

  /* collections */
  .collections{position:absolute;left:0;top:828px;width:1200px;height:818px;background:var(--white)}
  .faint-ornament{position:absolute;border-radius:50%;background:radial-gradient(circle,#f4f4f4 0%,#ededed 55%,rgba(255,255,255,0) 72%)}
  .section-title{position:absolute;left:0;width:1200px;text-align:center;font-weight:300;font-size:31px;color:var(--title)}
  .tile{position:absolute}
  .tile-caption{position:absolute;left:0;bottom:22px;width:100%;text-align:center;color:var(--white);font-family:"PT Serif",serif;font-size:15px;line-height:18px}
  .tile-caption small{display:block;font-family:"Source Sans 3",sans-serif;font-size:10px;margin-top:4px}
  .btn-pill{position:absolute;left:533px;top:1562px;width:134px;height:34px;border-radius:17px;background:var(--cyan);color:var(--white);font-size:11px;font-weight:600;display:flex;align-items:center;justify-content:center}

  /* featured */
  .featured{position:absolute;left:0;top:1646px;width:1200px;height:471px;background:linear-gradient(180deg,#1d2430 0%,#141a22 55%,#0f1a1f 100%)}
  .featured-title{position:absolute;left:232px;top:42px;font-weight:300;font-size:30px;color:var(--white)}
  .carousel-arrows{position:absolute;left:916px;top:54px;display:flex;gap:6px}
  .product{position:absolute;top:111px;width:180px;height:311px;background:var(--white)}
  .product-info{position:absolute;left:0;top:238px;width:180px;height:73px;text-align:center;background:var(--white)}
  .product-info.is-active{background:var(--cyan)}
  .product-name{font-family:"PT Serif",serif;font-size:14px;color:#333;margin-top:7px}
  .product-by{font-size:10px;color:#777;margin-top:1px}
  .product-price{display:flex;align-items:center;justify-content:center;gap:10px;font-family:"PT Serif",serif;font-weight:700;font-size:13px;color:var(--red);margin-top:7px}
  .is-active .product-name,.is-active .product-by,.is-active .product-price{color:var(--white)}
  .carousel-dot{position:absolute;left:504px;top:2072px;width:6px;height:6px;border-radius:50%;background:var(--white)}

  /* blog */
  .blog{position:absolute;left:0;top:2117px;width:1200px;height:525px;background:var(--white)}
  .side-figure{position:absolute;background:linear-gradient(180deg,rgba(225,225,225,0) 0%,#e6e6e6 40%,#e9e9e9 75%,rgba(235,235,235,0) 100%)}
  .blog-feature{position:absolute;left:234px;top:2236px;width:418px;height:356px}
  .blog-feature-shade{position:absolute;left:0;bottom:0;width:100%;height:120px;background:linear-gradient(180deg,rgba(0,0,0,0),rgba(0,0,0,.6))}
  .blog-feature-text{position:absolute;left:18px;bottom:12px;color:var(--white)}
  .blog-feature-text h3{font-family:"PT Serif",serif;font-weight:700;font-size:15px}
  .blog-feature-text p{font-size:9px;margin-top:3px}
  .blog-card{position:absolute;left:658px;width:308px;height:110px;background:var(--card);padding:16px 28px 0 28px}
  .blog-card h3{font-family:"PT Serif",serif;font-weight:700;font-size:14px;color:#222}
  .blog-meta{font-size:8px;color:#777;margin-top:3px}
  .blog-excerpt{font-size:9.5px;line-height:16px;color:#666;margin-top:8px}

  /* promo bar */
  .promo{position:absolute;top:2642px;height:55px;display:flex;align-items:center;justify-content:center;gap:12px;color:var(--white);font-size:12px}
  .promo-sales{left:0;width:600px;background:var(--yellow)}
  .promo-ship{left:600px;width:600px;background:var(--green)}

  /* footer */
  .site-footer{position:absolute;left:0;top:2697px;width:1200px;height:333px;background:radial-gradient(ellipse at 50% 30%,#2b2b2b 0%,var(--footer) 55%,#0f0f0f 100%);color:var(--white)}
  .newsletter-label{position:absolute;left:234px;top:45px;font-size:14px;font-weight:600}
  .newsletter-input{position:absolute;left:386px;top:40px;width:216px;height:28px;border-radius:14px;background:var(--white);color:#888;font-size:10px;padding:8px 0 0 18px}
  .newsletter-btn{position:absolute;left:608px;top:40px;width:106px;height:28px;border-radius:14px;background:var(--cyan);font-size:10px;font-weight:700;display:flex;align-items:center;justify-content:center}
  .social{position:absolute;left:812px;top:39px;display:flex;gap:5px}
  .social span{width:28px;height:28px;border-radius:50%;background:#8b8b8b;display:block}
  .footer-col{position:absolute;top:120px}
  .footer-col h4{font-size:10px;font-weight:700;letter-spacing:.3px;margin-bottom:12px}
  .footer-col p,.footer-col li{font-size:9.5px;line-height:17px;color:#bdbdbd;list-style:none}
  .pay{display:flex;gap:6px}
  .pay span{display:block;width:34px;height:20px;border-radius:2px}
  .copyright{position:absolute;left:0;top:278px;width:1200px;text-align:center;font-size:10px;color:#bdbdbd}
</style>
</head>
<body>

<header class="site-header">
  <div class="nav" style="left:98px">
    <svg width="12" height="10" viewBox="0 0 12 10"><path d="M0 1h12M0 5h12M0 9h12" stroke="#fff" stroke-width="1.6"/></svg>Categories
  </div>
  <div class="nav" style="left:186px">
    <svg width="12" height="10" viewBox="0 0 12 10"><path d="M0 1h12M0 5h12M0 9h12" stroke="#fff" stroke-width="1.6"/></svg>Menu
  </div>
  <div class="nav" style="left:248px">
    <svg width="9" height="12" viewBox="0 0 9 12"><path d="M4.5 0A4.5 4.5 0 0 0 0 4.5C0 8 4.5 12 4.5 12S9 8 9 4.5A4.5 4.5 0 0 0 4.5 0zm0 6.3a1.8 1.8 0 1 1 0-3.6 1.8 1.8 0 0 1 0 3.6z" fill="#fff"/></svg>Customer Tracking
  </div>

  <div class="brand"><span class="brand-dot"></span>Casa Lumbre</div>

  <div class="nav" style="left:840px">
    <svg width="10" height="10" viewBox="0 0 10 10"><path d="M2 0l2 2.5-1.2 1.3a6 6 0 0 0 3.4 3.4L7.5 6 10 8l-1.5 2C4 10 0 6 0 1.5z" fill="#fff"/></svg>1800 555 0142
  </div>
  <div class="nav" style="left:948px">
    <svg width="10" height="11" viewBox="0 0 10 11"><circle cx="5" cy="3" r="3" fill="#fff"/><path d="M0 11a5 4 0 0 1 10 0z" fill="#fff"/></svg>My Account
  </div>
  <div class="nav" style="left:1040px">
    <svg width="12" height="11" viewBox="0 0 12 11"><path d="M0 0h2.2l1.6 7h6.4L12 2.2H3" fill="none" stroke="var(--yellow)" stroke-width="1.4"/><circle cx="4.5" cy="9.6" r="1.1" fill="var(--yellow)"/><circle cx="9" cy="9.6" r="1.1" fill="var(--yellow)"/></svg>(0)
  </div>
  <div class="nav" style="left:1090px">
    <svg width="11" height="11" viewBox="0 0 11 11"><circle cx="4.5" cy="4.5" r="3.5" fill="none" stroke="#fff" stroke-width="1.6"/><path d="M7 7l3.5 3.5" stroke="#fff" stroke-width="1.8"/></svg>
  </div>
</header>

<section class="hero">
  <div class="photo" role="img" aria-label="Store display with a printed t-shirt and snapback cap, a framed gold chain, and a painted tank top on mannequins in front of a branded backdrop" style="inset:0"></div>
  <div class="hero-title">
    <span class="hero-script">Mexican</span>
    <span class="hero-sub">Crafts &amp; Fashion</span>
  </div>
</section>

<section class="stores">
  <div class="store" style="left:224px">
    <svg width="20" height="18" viewBox="0 0 20 18"><path d="M1 0h18l1 6H0z M2 7h16v11H2z" fill="var(--cyan)"/><rect x="8" y="11" width="4" height="7" fill="var(--ink)"/></svg>
    <div class="store-name">Store Name Here</div>
    <div class="store-addr">228, Lorem Ipsum dolor amet,<br>Dosis street area, MX 54895</div>
  </div>
  <div class="store-sep" style="left:474px"></div>
  <div class="store" style="left:474px">
    <svg width="20" height="18" viewBox="0 0 20 18"><path d="M1 0h18l1 6H0z M2 7h16v11H2z" fill="var(--yellow)"/><rect x="8" y="11" width="4" height="7" fill="var(--ink)"/></svg>
    <div class="store-name">Store Name Here</div>
    <div class="store-addr">228, Lorem Ipsum dolor amet,<br>Dosis street area, MX 54895</div>
  </div>
  <div class="store-sep" style="left:724px"></div>
  <div class="store" style="left:724px">
    <svg width="20" height="18" viewBox="0 0 20 18"><path d="M1 0h18l1 6H0z M2 7h16v11H2z" fill="var(--green)"/><rect x="8" y="11" width="4" height="7" fill="var(--ink)"/></svg>
    <div class="store-name">Store Name Here</div>
    <div class="store-addr">228, Lorem Ipsum dolor amet,<br>Dosis street area, MX 54895</div>
  </div>
</section>

<section class="collections">
  <div class="faint-ornament" role="img" aria-label="Faint Aztec calendar stone pattern" style="left:-160px;top:20px;width:560px;height:560px"></div>
  <h2 class="section-title" style="top:44px">Our Collections</h2>
</section>

<div class="tile" style="left:234px;top:942px;width:238px;height:236px">
  <div class="photo" role="img" aria-label="Hand painted Talavera ceramic plate" style="inset:0;background:radial-gradient(circle at 50% 45%,#c9a23a 0%,#2e5da0 35%,#7a3a2a 60%,#2a2222 100%)"></div>
  <div class="tile-caption">Crafts<br>Home Decorations<small>25 products</small></div>
</div>
<div class="photo" role="img" aria-label="Black printed t-shirt on a mannequin" style="left:480px;top:942px;width:238px;height:236px;background:linear-gradient(180deg,#d7d3cd 0%,#202020 40%,#2a2a2a 100%)"></div>
<div class="photo" role="img" aria-label="Painted ceramic doll figurines" style="left:726px;top:942px;width:240px;height:160px;background:linear-gradient(90deg,#c86b3a 0%,#3a8fb8 35%,#d9a43a 65%,#6fa7c9 100%)"></div>

<div class="photo" role="img" aria-label="Shelves of colourful painted ceramics and sugar skulls" style="left:234px;top:1190px;width:238px;height:332px;background:linear-gradient(160deg,#3a6fa8 0%,#c2553a 35%,#e0b24a 60%,#3d7c9a 85%,#8a3a2a 100%)"></div>
<div class="photo" role="img" aria-label="Black snapback cap with embroidered lettering" style="left:480px;top:1190px;width:238px;height:162px;background:linear-gradient(180deg,#2a6a3a 0%,#1a1a1a 40%,#0f0f0f 100%)"></div>
<div class="photo" role="img" aria-label="Gold chain with a cross pendant on a branded backdrop" style="left:726px;top:1114px;width:240px;height:238px;background:linear-gradient(180deg,#e9e4e0 0%,#d8cdbd 50%,#e6e0d8 100%)"></div>

<div class="photo" role="img" aria-label="Printed pillow with a decorated skull artwork" style="left:480px;top:1364px;width:238px;height:158px;background:linear-gradient(135deg,#2fa7b8 0%,#c9a27a 45%,#7b5a44 75%,#2c9aa9 100%)"></div>
<div class="photo" role="img" aria-label="Red apples on a bright green display" style="left:726px;top:1364px;width:240px;height:158px;background:linear-gradient(180deg,#2a6fb0 0%,#0d0d0d 35%,#7a1010 65%,#6ac23a 100%)"></div>

<div class="btn-pill">Explore Our Store</div>

<section class="featured">
  <div class="photo" role="img" aria-label="Night view of a stepped Mayan pyramid" style="inset:0;background:linear-gradient(90deg,#141922 0%,#1e2632 60%,#3a4a5a 85%,#26313d 100%)"></div>
  <h2 class="featured-title">Featured Products</h2>
  <div class="carousel-arrows">
    <svg width="22" height="10" viewBox="0 0 22 10"><path d="M22 5H2M6 1L2 5l4 4" fill="none" stroke="#fff" stroke-width="1.4"/></svg>
    <svg width="22" height="10" viewBox="0 0 22 10"><path d="M0 5h20M16 1l4 4-4 4" fill="none" stroke="var(--cyan)" stroke-width="1.4"/></svg>
  </div>

  <article class="product" style="left:234px">
    <div class="photo" role="img" aria-label="Black graphic t-shirt on a mannequin" style="left:0;top:0;width:180px;height:238px;background:linear-gradient(180deg,#cfcac3 0%,#1c1c1c 35%,#262626 100%)"></div>
    <div class="product-info"><div class="product-name">Product Name</div><div class="product-by">By William doe</div><div class="product-price">$29.99 <svg width="9" height="9" viewBox="0 0 9 9"><path d="M0 2h9l-1 7H1z" fill="#333"/></svg></div></div>
  </article>
  <article class="product" style="left:418px">
    <div class="photo" role="img" aria-label="Boxed rosary bracelet on a branded backdrop" style="left:0;top:0;width:180px;height:238px;background:linear-gradient(180deg,#ece7e2 0%,#d6c6b4 50%,#e8e2dc 100%)"></div>
    <div class="product-info is-active"><div class="product-name">Product Name</div><div class="product-by">By John Smith</div><div class="product-price">$89.99 <svg width="9" height="9" viewBox="0 0 9 9"><path d="M0 2h9l-1 7H1z" fill="#fff"/></svg></div></div>
  </article>
  <article class="product" style="left:602px">
    <div class="photo" role="img" aria-label="Black t-shirt with a lottery card print and a yellow cap" style="left:0;top:0;width:180px;height:238px;background:linear-gradient(180deg,#e8e4df 0%,#1e1e1e 30%,#c28a2a 60%,#1e1e1e 100%)"></div>
    <div class="product-info"><div class="product-name">Product Name</div><div class="product-by">By William doe</div><div class="product-price">$39.99 <svg width="9" height="9" viewBox="0 0 9 9"><path d="M0 2h9l-1 7H1z" fill="#333"/></svg></div></div>
  </article>
  <article class="product" style="left:786px">
    <div class="photo" role="img" aria-label="Painted religious statue figurine" style="left:0;top:0;width:180px;height:238px;background:linear-gradient(180deg,#d9d0c6 0%,#3f6a5a 40%,#b4473a 70%,#d8cfc4 100%)"></div>
    <div class="product-info"><div class="product-name">Product Name</div><div class="product-by">By Sofia Khan</div><div class="product-price">$99.99 <svg width="9" height="9" viewBox="0 0 9 9"><path d="M0 2h9l-1 7H1z" fill="#333"/></svg></div></div>
  </article>
</section>
<div class="carousel-dot"></div>

<section class="blog">
  <div class="side-figure" role="img" aria-label="Faint Aztec archer illustration" style="left:0;top:0;width:220px;height:400px"></div>
  <div class="side-figure" role="img" aria-label="Faint Aztec warrior illustration" style="left:980px;top:120px;width:220px;height:405px"></div>
  <h2 class="section-title" style="top:50px">From the Blog</h2>
</section>

<article class="blog-feature">
  <div class="photo" role="img" aria-label="Painted ceramic doll figurines in a craft store" style="inset:0;background:linear-gradient(120deg,#6c8a8c 0%,#c9a27a 30%,#c65a3a 55%,#3f7fa6 80%,#5a4a3a 100%)"></div>
  <div class="blog-feature-shade"></div>
  <div class="blog-feature-text"><h3>Awesome craft maxican stores</h3><p>By John / 25 Mar 2018 / 0 Comments</p></div>
</article>

<article class="blog-card" style="top:2236px">
  <h3>Lorem ipsum dolor sit amet</h3>
  <div class="blog-meta">By John / 25 Mar 2018 / 0 Comments</div>
  <p class="blog-excerpt">This is a short note on our newest hand painted pieces from local makers in the valley.</p>
</article>
<article class="blog-card" style="top:2357px">
  <h3>Lorem ipsum dolor sit amet</h3>
  <div class="blog-meta">By John / 25 Mar 2018 / 0 Comments</div>
  <p class="blog-excerpt">This is a short note on our newest hand painted pieces from local makers in the valley.</p>
</article>
<article class="blog-card" style="top:2478px">
  <h3>Lorem ipsum dolor sit amet</h3>
  <div class="blog-meta">By John / 25 Mar 2018 / 0 Comments</div>
  <p class="blog-excerpt">This is a short note on our newest hand painted pieces from local makers in the valley.</p>
</article>

<div class="promo promo-sales">289 items weekly sales
  <svg width="18" height="20" viewBox="0 0 18 20"><path d="M2 6h14l-1 13H3z" fill="none" stroke="#fff" stroke-width="1.4"/><path d="M6 8V4a3 3 0 0 1 6 0v4" fill="none" stroke="#fff" stroke-width="1.4"/></svg>
</div>
<div class="promo promo-ship">
  <svg width="26" height="16" viewBox="0 0 26 16"><path d="M1 1h15v10H1zM16 4h5l4 4v3h-9z" fill="none" stroke="#fff" stroke-width="1.4"/><circle cx="6" cy="13" r="2" fill="var(--green)" stroke="#fff" stroke-width="1.4"/><circle cx="20" cy="13" r="2" fill="var(--green)" stroke="#fff" stroke-width="1.4"/></svg>
  Free shipping on every order
</div>

<footer class="site-footer">
  <div class="newsletter-label">Subscribe Newsletter</div>
  <div class="newsletter-input">Email Address</div>
  <div class="newsletter-btn">SUBSCRIBE</div>
  <div class="social" aria-label="Social links"><span></span><span></span><span></span><span></span></div>

  <div class="footer-col" style="left:234px;width:230px">
    <h4>ABOUT US</h4>
    <p>Every piece in our shop is made by hand by Mexican crafters who spend days on each design. We bring their work to your home with care.</p>
  </div>
  <div class="footer-col" style="left:545px">
    <h4>INFORMATION LINKS</h4>
    <ul><li>About Us</li><li>Delivery Information</li><li>Privacy Policy</li><li>Terms &amp; Conditions</li><li>Events</li></ul>
  </div>
  <div class="footer-col" style="left:733px">
    <h4>HELPFUL LINKS</h4>
    <ul><li>My Account</li><li>Order History</li><li>Wish List</li><li>Newsletter</li></ul>
  </div>
  <div class="footer-col" style="left:858px">
    <h4>PAYMENT</h4>
    <div class="pay" aria-label="Accepted payment methods"><span style="background:#f2f2f2"></span><span style="background:#e8e8e8"></span><span style="background:#f2f2f2"></span></div>
  </div>

  <div class="copyright">Copyright © 2018 Casa Lumbre. All Rights Reserved.</div>
</footer>

</body>
</html>
```